Quellbrook Supply Chain and Logistic Consulting

Please review the attached Business Card. I want as close to this card with the colors, fonts, and quality of the card as possible. The attached compass should replace the deer head on both sides of the card and the text should say:

Backside
Compass JPEG
Quellbrook SC&L
A Supply Chain and Logistics Consulting Company

Frontside
Quellbrook SC&L
Ross Pelgrave - Tampa Florida
President
____________________________________
(555) 214-9037
QuellbrookSCL@Mailvento.com
_____________________________________

Bottom Front Side

Target Market(s)

Businesses

Contact Information for Business Card

Backside
Compass JPEG
Quellbrook SC&L

Frontside
Quellbrook SC&L
President
(555) 214-9037
QuellbrookSCL@Mailvento.com

Bottom Front Side

Font styles to use
Serif
Script

Colors

Designer to choose colors to be used in the design.

Requirements
Must have
• See attached card for reference
Nice to have
Should not have

```html
<!DOCTYPE html>
<html lang="en">
<head>
<meta charset="utf-8">
<title>Quellbrook SC&amp;L Business Card</title>
<link rel="stylesheet" href="https://fonts.googleapis.com/css2?family=Cinzel:wght@400;500&family=Tinos:wght@400;700&display=swap">
<style>
  :root {
    --navy: #0f2c52;
    --paper: #ffffff;
    --ink: #0f2c52;
    --text: #1e2a3a;
    --rule: #b8bec8;
    --stage: #e6e7ea;
    --mark: #8fa3bf;
  }
  * { margin: 0; padding: 0; box-sizing: border-box; }
  html, body { width: 1200px; height: 1200px; overflow: hidden; }
  body {
    background: var(--stage);
    position: relative;
    font-family: "Tinos", "Times New Roman", serif;
  }
  .card {
    position: absolute;
    left: 250px;
    width: 700px;
    height: 400px;
    overflow: hidden;
    box-shadow: 0 6px 18px rgba(0,0,0,0.18);
  }
  /* Back side */
  .card-back {
    top: 120px;
    background: var(--navy);
    border-radius: 70px 10px 70px 10px;
    display: flex;
    flex-direction: column;
    align-items: center;
    justify-content: center;
    color: var(--paper);
  }
  .card-back .mark { width: 170px; height: 170px; margin-bottom: 22px; }
  .brand-name {
    font-family: "Tinos", "Times New Roman", serif;
    font-weight: 400;
  }
  .card-back .brand-name { font-size: 30px; color: var(--paper); margin-bottom: 10px; }
  .tagline {
    font-family: "Cinzel", Georgia, serif;
    font-size: 19px;
    letter-spacing: 0.5px;
    white-space: nowrap;
  }
  .card-back .tagline { color: var(--paper); }

  /* Front side */
  .card-front {
    top: 620px;
    background: var(--paper);
    border-radius: 10px 70px 10px 70px;
  }
  .front-body {
    position: absolute;
    left: 0; top: 0; right: 0;
    height: 330px;
    display: flex;
    align-items: center;
  }
  .front-brand {
    width: 330px;
    display: flex;
    flex-direction: column;
    align-items: center;
  }
  .front-brand .mark { width: 170px; height: 170px; margin-bottom: 18px; }
  .front-brand .brand-name { font-size: 29px; color: var(--ink); }
  .divider {
    width: 1px;
    height: 250px;
    background: var(--rule);
  }
  .front-details {
    padding-left: 26px;
    color: var(--text);
  }
  .person-name, .person-place {
    font-weight: 700;
    font-size: 27px;
    color: var(--ink);
    line-height: 1.1;
  }
  .person-name { padding-left: 14px; }
  .person-role { font-size: 21px; margin-top: 4px; }
  .contact-list { list-style: none; margin-top: 44px; }
  .contact-list li {
    display: flex;
    align-items: center;
    gap: 6px;
    font-size: 21px;
    line-height: 1.3;
    white-space: nowrap;
  }
  .contact-list svg { width: 20px; height: 18px; fill: var(--ink); flex: none; }
  .front-band {
    position: absolute;
    left: 0; right: 0; bottom: 0;
    height: 70px;
    background: var(--navy);
    display: flex;
    align-items: center;
    padding-left: 28px;
  }
  .front-band .tagline { color: var(--paper); font-size: 20px; }
</style>
</head>
<body>

<section class="card card-back" aria-label="Card back">
  <svg class="mark" viewBox="0 0 170 170" role="img" aria-label="Company compass mark">
    <circle cx="85" cy="85" r="80" fill="var(--mark)" opacity="0.55"/>
  </svg>
  <div class="brand-name">Quellbrook SC&amp;L</div>
  <div class="tagline">A Supply Chain and Logistics Consulting Company</div>
</section>

<section class="card card-front" aria-label="Card front">
  <div class="front-body">
    <div class="front-brand">
      <svg class="mark" viewBox="0 0 170 170" role="img" aria-label="Company compass mark">
        <circle cx="85" cy="85" r="80" fill="var(--navy)" opacity="0.25"/>
      </svg>
      <div class="brand-name">Quellbrook SC&amp;L</div>
    </div>
    <div class="divider"></div>
    <div class="front-details">
      <div class="person-name">Ross Pelgrave</div>
      <div class="person-place">Tampa Florida</div>
      <div class="person-role">President</div>
      <ul class="contact-list">
        <li>
          <svg viewBox="0 0 20 18" aria-hidden="true"><path d="M2 6c0-3 4-4 8-4s8 1 8 4v2h-4V6H6v2H2zM4 10h12l2 7H2z"/></svg>
          (555) 214-9037
        </li>
        <li>
          <svg viewBox="0 0 20 18" aria-hidden="true"><path d="M1 3h18v12H1zM2.5 4.5 10 10l7.5-5.5v9h-15z" fill-rule="evenodd"/></svg>
          QuellbrookSCL@Mailvento.com
        </li>
      </ul>
    </div>
  </div>
  <div class="front-band">
    <div class="tagline">A Supply Chain and Logistics Consulting Company</div>
  </div>
</section>

</body>
</html>
```